Folded Business Cards, Envelopes, Information card and Thank You card.
Gala Tent Company
Folded Business Cards, Envelopes, Information card and Thank You card. - Events
Creative Brief
Modern
Marisol Fenwick-Dutra
Owner-Linen Specialist
2718 Harbor Crest Ave Suite 204B Long Beach CA 90807
marisol@larkspurdrapery.example
larkspurdraperys.example
Our colors are silver, grey, dark plum and eggplant. I would like something modern with maybe translucent floral scrolls in the background. I am open to card back ground color. It can be silver, plum/eggplant or even white. We are a high-end wedding linen rental company. Our clients are mostly female, mid income and are planning a wedding. I am looking for the following items: 1. Business Card. 2. Envelope. 3. Information Card. 4. Thank You Card. Information Card: This is an information card that will be sent out with each order. It will be printed on a 6" x 9" post card one sided. Bellow is the text that will go on the card Important Information Regarding Your Linen Returns. Thank you for allowing Larkspur Drapery linens to share in your special day. To ensure prompt return of your linens, please follow the steps bellow. 1. Please place all linens in the included return duffel bags or the box they arrived in. It returning in a box, please fold linens so that they all fit in the box. Please shake any loose food from linens and insure linens are dry prior to placing in box and bags. NEVER place wet linens in bags, boxes of plastic. If your linens are wet or damp please allow them to air dry prior to packing. If your shipment included chair sashes, please remember to untie each sash prior to return. You account will be billed a fee of $.25 for each sash returned that is untied. 2. If you would like to schedule a ParcelWing pickup, please contact ParcelWing the day PRIOR to your scheduled return date as ParcelWing does not do same pickup. Please note, ParcelWing charges a pickup fee of $8. This fee is paid directly to ParcelWing. You can contact ParcelWing at 1.800.Go.Wing (555-0148). You may also return your linens for free of charge by dropping of your linens at any ParcelWing or ParcelWing Copyhub. Please use the attached pre-paid ParcelWing air-bil that came with your shipment. Lost ParcelWing Air-Bills: Please treat your ParcelWing return air-bills as cash. If they are lost or damaged, please contact us as soon as possible for replacements. We charge a fee of $25 for each lost or damaged air-bill that needs to be replaced. Alternate Shipping Carriers: Your linen rental includes pre-paid return shipping via ParcelWing and include tracking for our warehouse. Please do not return linens using any other shipping provider or any other class of shipping (i.e. Express, Next Day, Over Night these services will be billed back to your account). Late Returns: Our customers depend on your timely return. Please insure our items are dropped off or picked up by ParcelWing the following business day after your event. Items shipped back after the due date are considered late and will be charge a rental fee equal to 50% of your original rental rate prior to any discounts or promotions. Should you have any questions regarding your order please contact our office at 562.555.0173 should you need to reach us after hours or on weekends please leave a message or send an e-mail to afterhours@larkspurdraperys.example. Thank you card: Please also design a matching thank you card that will be printed on a 4" x 6" one sided post card.
Notes: We are using a folded business card: We would like it laid out as follows: Front: Logo with contact details Inside: The inside will have a space where we can glue on a fabric swatch. We would like the swatch to be placed placed in a decorative rectangle that should take up most of the inside. There also needs to be wording under the square that says "Raspberry Satin Back Shantung" we would like this centered. Back: On the back of the card we would like: twitter icon with our twitter id:larkspurcloth youtube logo with our id: larkspurdraperys

```html
<!DOCTYPE html>
<html lang="en">
<head>
<meta charset="utf-8">
<title>Larkspur Drapery – Folded Business Card</title>
<link rel="stylesheet" href="https://fonts.googleapis.com/css2?family=Open+Sans:wght@400;600;700&family=Cormorant+Garamond:wght@500&display=swap">
<style>
  :root{
    --backdrop:#e6e4e1;
    --card-grey:#7b7b7b;
    --card-white:#ffffff;
    --plum:#5b2b5f;
    --text-grey:#6e6e6e;
    --logo-grey:#7a7a7a;
    --accent-bar:#8a8a8a;
    --on-grey:#ffffff;
  }
  *{box-sizing:border-box;margin:0;padding:0}
  html,body{width:1200px;height:874px;overflow:hidden}
  body{background:var(--backdrop);font-family:"Open Sans",Arial,sans-serif;position:relative}

  .card-half{position:absolute;border-radius:22px;overflow:hidden;box-shadow:0 6px 18px rgba(0,0,0,.18)}

  /* Folded card – outside */
  .outer-back{left:115px;top:175px;width:418px;height:267px;background:var(--card-grey)}
  .outer-front{left:115px;top:446px;width:418px;height:264px;background:var(--card-white)}

  /* Folded card – inside */
  .inner-swatch{left:636px;top:175px;width:463px;height:267px;background:var(--card-white)}
  .inner-caption{left:636px;top:446px;width:463px;height:264px;background:var(--card-grey)}

  /* Back panel: printed upside-down so it reads correctly once folded */
  .social-block{position:absolute;inset:0;transform:rotate(180deg)}
  .social-list{position:absolute;right:44px;bottom:18px;list-style:none}
  .social-item{display:flex;align-items:center;gap:8px;color:var(--on-grey);font-size:15px;line-height:20px;justify-content:flex-end}
  .social-icon{width:14px;height:14px;background:var(--on-grey);opacity:.85;border-radius:2px}

  /* Front panel */
  .contact-name{position:absolute;left:41px;top:42px;font-size:17px;font-weight:700;color:var(--plum)}
  .contact-title{position:absolute;left:41px;top:66px;font-size:13px;color:var(--text-grey)}
  .contact-details{position:absolute;left:41px;top:130px;font-size:9.5px;line-height:12.5px;color:var(--text-grey);font-style:normal}
  .contact-details b{font-weight:700}
  .contact-web{position:absolute;left:41px;top:222px;font-size:12px;color:var(--text-grey)}
  .accent-bar{position:absolute;left:0;top:128px;width:9px;height:72px;background:var(--accent-bar)}

  .brand-mark{position:absolute;left:307px;top:72px;width:72px;height:68px;background:var(--logo-grey)}
  .brand-name{position:absolute;left:250px;top:150px;width:185px;text-align:center;font-family:"Cormorant Garamond",Georgia,serif;font-weight:500;color:var(--logo-grey);line-height:1}
  .brand-name .line-main{display:block;font-size:27px;letter-spacing:1px}
  .brand-name .line-sub{display:block;font-size:13px;letter-spacing:3px;margin-top:3px}

  /* Inside caption */
  .swatch-caption{position:absolute;left:0;right:0;top:88px;text-align:center;font-family:"Cormorant Garamond",Georgia,serif;font-weight:500;font-size:21px;color:var(--on-grey)}
</style>
</head>
<body>

  <section class="card-half outer-back" aria-label="Card back">
    <div class="social-block">
      <ul class="social-list">
        <li class="social-item"><span class="social-icon"></span><span>larkspurcloth</span></li>
        <li class="social-item"><span class="social-icon"></span><span>larkspurdraperys</span></li>
      </ul>
    </div>
  </section>

  <section class="card-half outer-front" aria-label="Card front">
    <h1 class="contact-name">Marisol Fenwick-Dutra</h1>
    <p class="contact-title">Owner-Linen Specialist</p>
    <span class="accent-bar"></span>
    <address class="contact-details">
      2718 Harbor Crest Ave<br>
      Suite 204B<br>
      Long Beach CA 90807<br>
      <b>Phone:</b> 562.555.0173<br>
      <b>Fax:</b> 562.555.0190<br>
      <b>Email:</b> marisol@larkspurdrapery.example
    </address>
    <p class="contact-web">www.larkspurdraperys.example</p>
    <span class="brand-mark"></span>
    <p class="brand-name"><span class="line-main">LARKSPUR</span><span class="line-sub">DRAPERY</span></p>
  </section>

  <section class="card-half inner-swatch" aria-label="Fabric swatch area"></section>

  <section class="card-half inner-caption">
    <p class="swatch-caption">Raspberry Satin Back Shantung</p>
  </section>

</body>
</html>
```